Brightmoor Fire Solutions business card, logo and web design.

We need business cards for our new company. We are based in South Africa. We specialise in fire detection, fire prevention, security, access control and CCTV in buildings. We service and install sprinkler systems, fire hose reals and fire extinguishers in buildings. Our slogan in the company is "Safety built into every floor" . We strive to be innovators in our field and deliver the best service possible at the best quality. We want to be the best in our field. We don't have any colour preferences as long as it relates to our type of business.
Our target market is clients that owns big buildings with multiple levels, such a malls,office buildings or warehouses.

Target Market(s)

Industry/Entity Type

Fire Safety

Contact Information for Business Card

The front of the card should have the company name (Brightmoor Fire Solutions (PTY) LTD. and a description of the company. Fire engineering & security services.

Logo Text

Safety built into every floor

Number of Pages Required

4 page

Font styles to use
Serif

Colors

Designer to choose colors to be used in the design.

Requirements
Must have
• The company name, the logo and all the details on the back of the card. It should be simple and not to busy.
Nice to have
• Just something different and new. Brightmoor means - innovate so the card should represent our name.
Should not have
• Small pictures or lots of graphics on.

```html
<!DOCTYPE html>
<html lang="en">
<head>
<meta charset="utf-8">
<title>Brightmoor Fire Solutions – Business Card</title>
<link href="https://fonts.googleapis.com/css2?family=Lato:wght@300;400;700&display=swap" rel="stylesheet">
<style>
  :root{
    --red:#c8202c;
    --red-light:#d9444f;
    --red-dark:#a3131d;
    --white:#ffffff;
    --paper:#f4f4f4;
    --grey:#9a9a9a;
    --rule:#d8d8d8;
    --backdrop:#2a2a2a;
  }
  *{margin:0;padding:0;box-sizing:border-box}
  html,body{width:1200px;height:900px;overflow:hidden}
  body{
    background:var(--backdrop);
    font-family:'Lato',sans-serif;
    display:flex;flex-direction:column;align-items:center;justify-content:center;gap:40px;
  }
  .card{width:700px;height:390px;border-radius:28px;position:relative;overflow:hidden}

  /* Front */
  .card-front{
    background:radial-gradient(ellipse at 45% 40%,var(--red-light) 0%,var(--red) 55%,var(--red-dark) 100%);
    color:var(--white);
    display:flex;flex-direction:column;align-items:center;justify-content:center;
  }
  .front-name{font-weight:700;font-size:40px;letter-spacing:1px;line-height:1;white-space:nowrap}
  .front-rule{width:330px;height:2px;background:var(--white);margin-top:34px;opacity:.9}
  .front-tagline{font-weight:400;font-size:17px;letter-spacing:1.5px;margin-top:10px;text-transform:uppercase}

  /* Back */
  .card-back{background:linear-gradient(160deg,var(--white) 0%,var(--paper) 100%)}
  .back-brand{position:absolute;left:40px;top:44px}
  .back-brand .name{color:var(--red);font-weight:700;font-size:30px;line-height:1;letter-spacing:.5px;white-space:nowrap}
  .back-brand .reg{color:var(--grey);font-size:11px;letter-spacing:1px;margin-top:12px}
  .person{position:absolute;right:56px;top:150px;text-align:right}
  .person .who{color:var(--red);font-weight:700;font-size:22px;letter-spacing:1px}
  .person .role{color:var(--grey);font-size:12px;letter-spacing:2px;margin-top:2px}
  .person-bar{position:absolute;right:26px;top:148px;width:14px;height:46px;background:var(--red)}
  .contact-band{
    position:absolute;left:0;right:0;bottom:30px;height:110px;background:var(--red);
    border-top:4px solid var(--rule);
    color:var(--white);font-size:14px;letter-spacing:.5px;
    display:grid;grid-template-columns:1.1fr 1.6fr 1fr;column-gap:14px;row-gap:12px;
    padding:22px 30px;align-content:center;
  }
  .contact{display:flex;align-items:center;gap:9px;white-space:nowrap}
  .contact svg{width:14px;height:14px;flex:none;fill:var(--white)}
  .contact-wide{grid-column:span 2}
</style>
</head>
<body>
  <section class="card card-front" aria-label="Card front">
    <div class="front-name">BRIGHTMOOR FIRE SOLUTIONS</div>
    <div class="front-rule"></div>
    <div class="front-tagline">Safety built into every floor</div>
  </section>

  <section class="card card-back" aria-label="Card back">
    <div class="back-brand">
      <div class="name">BRIGHTMOOR FIRE SOLUTIONS</div>
      <div class="reg">VAT NO. 4710384526. REG NO. 21/30572/07</div>
    </div>
    <div class="person">
      <div class="who">DANIEL VERSTER</div>
      <div class="role">MANAGING DIRECTOR</div>
    </div>
    <div class="person-bar"></div>

    <div class="contact-band">
      <div class="contact">
        <svg viewBox="0 0 16 16"><path d="M4 0h8a1 1 0 0 1 1 1v14a1 1 0 0 1-1 1H4a1 1 0 0 1-1-1V1a1 1 0 0 1 1-1zm1 2v10h6V2zm3 11a1 1 0 1 0 0 2 1 1 0 0 0 0-2z"/></svg>
        +27 (0)12 555 0142
      </div>
      <div class="contact">
        <svg viewBox="0 0 16 16"><path d="M1 5a2 2 0 0 1 2-2c1 0 3 3 3 4s-2 1-1 3 2 3 3 3 1-2 3-1 4 2 4 3a2 2 0 0 1-2 2C7 17-1 9 1 5z"/></svg>
        +27 (0)12 555 0178
      </div>
      <div class="contact">
        <svg viewBox="0 0 16 16"><path d="M4 0h8v4H4zM1 5h14v7h-3v4H4v-4H1zm5 5v4h4v-4z"/></svg>
        +27 (0)83 555 0193
      </div>
      <div class="contact">
        <svg viewBox="0 0 16 16"><path d="M0 3h16v10H0zm1.5 1.2L8 9l6.5-4.8V4h-13z"/></svg>
        hello@brightmoorfire.co.za
      </div>
      <div class="contact contact-wide">
        <svg viewBox="0 0 16 16"><path d="M8 1l8 7h-2.5v7h-4v-4h-3v4h-4V8H0z"/></svg>
        14 Kestrel Avenue. Lynnwood. Pretoria. 0081
      </div>
    </div>
  </section>
</body>
</html>
```